Graphical design for food product in 1 Liter carton

We need this design not for a real product but as a showcase for a new service.

This special situation makes it really simple for you to participate because you only have to care about how the visual impression of your design is.

Furthermore it gives you the opportunity to get an extra winning chance if you choose to also participate in the open competition at our website - where you can enter the same design as you enter here at ArtForge.

Here is the requirements:

1. You must apply your design to our attatched template

2. Make a design for a food product of your own choice, which is to be sold from retail stores in a rectangular 1 L carton – based on our template.

3. You are only allowed to use brand names and/or logos that you have the rights to use for this competition, so please make completely fictive brand names and logos.

4. Your design is evaluated on the visual impression only, which means that your text on the design can be in any language and doesn’t have to relate to the design.

5. The criteria for the evaluation of your design is your creativity, the graphical quality and how well the product will display it self in the stores.

If you also want to participate in the open competition on our website - where you can win an SlateTab Lite, and will get your design skills exposed to brand owners and packaging manufacturers all over the world, then please visit spinomodel.example/packaging-design-competition/

Attatched is:

A. Empty design template you must apply your design to. Remove the layer with our template when you return your send in your design.

B. Example of design applied to the template.

C. Example of the applied example design after it has been converted to 3D with our online 3D engine at SpinoModel.example.

The winning design will be converted to 3D and will be used as a showcase on our website - all designers can enter their design to our open competition at SpinoModel.example.

```html
<!DOCTYPE html>
<html lang="en">
<head>
<meta charset="utf-8">
<title>Orvelo Orange Juice – 1 L carton</title>
<link rel="stylesheet" href="https://fonts.googleapis.com/css2?family=Josefin+Slab:wght@400;700&family=Playfair+Display:wght@600&family=Roboto:wght@400&display=swap">
<style>
  :root {
    --paper: #f7f7f7;
    --orange: #f07a3a;
    --green: #86c440;
    --text-grey: #7a7a7a;
    --white: #ffffff;
    --badge-grey: #8d8d8d;
  }
  * { margin: 0; padding: 0; box-sizing: border-box; }
  html, body {
    width: 1142px;
    height: 1200px;
    overflow: hidden;
    background: var(--paper);
  }
  .carton {
    position: relative;
    width: 1142px;
    height: 1200px;
    background: var(--paper);
  }
  .panel {
    position: absolute;
    top: 0;
    width: 576px;
    height: 1200px;
  }
  .panel--front { left: 0; }
  .panel--side { left: 576px; }

  .top-band {
    position: absolute;
    left: 0;
    top: 0;
    width: 288px;
    height: 70px;
    background: var(--orange);
    border-top: 8px solid var(--green);
  }
  .brand-name {
    position: absolute;
    left: 22px;
    top: 252px;
    font-family: "Josefin Slab", serif;
    font-weight: 700;
    font-size: 27px;
    color: var(--green);
  }
  .product-title {
    position: absolute;
    left: 20px;
    top: 305px;
    font-family: "Playfair Display", serif;
    font-weight: 600;
    font-size: 72px;
    line-height: 70px;
    color: var(--orange);
  }
  .product-copy {
    position: absolute;
    left: 22px;
    top: 478px;
    width: 260px;
    font-family: "Josefin Slab", serif;
    font-size: 18px;
    line-height: 25px;
    color: var(--text-grey);
  }
  .fruit {
    position: absolute;
    left: 30px;
    top: 612px;
    width: 230px;
    height: 320px;
  }
  .volume-badge {
    position: absolute;
    left: 234px;
    top: 968px;
    width: 33px;
    height: 48px;
    border-radius: 2px;
    background: linear-gradient(180deg, #b5b5b5, var(--badge-grey));
  }
  .tree-illustration {
    position: absolute;
    left: 318px;
    top: 308px;
    width: 234px;
    height: 712px;
    border-radius: 110px 110px 12px 12px;
    background: linear-gradient(180deg, #a8d872 0%, #c3e49c 45%, #e6f2d6 100%);
  }
  .variety-label {
    position: absolute;
    left: 446px;
    top: 790px;
    font-family: "Roboto", sans-serif;
    font-size: 18px;
    line-height: 21px;
    text-transform: uppercase;
  }
  .variety-label .line--green { color: var(--green); display: block; }
  .variety-label .line--orange { color: var(--orange); display: block; }
</style>
</head>
<body>
<main class="carton">
  <section class="panel panel--front">
    <div class="top-band"></div>
    <div class="brand-name">Orvelo</div>
    <h1 class="product-title">orange<br>juice</h1>
    <p class="product-copy">Donec eu pharetra lacus mollis blandit neque vulputate semper</p>
    <svg class="fruit" viewBox="0 0 230 320" aria-hidden="true">
      <defs>
        <radialGradient id="shadow-front" cx="50%" cy="50%" r="50%">
          <stop offset="0%" stop-color="#bdbdbd"/>
          <stop offset="100%" stop-color="#bdbdbd" stop-opacity="0"/>
        </radialGradient>
      </defs>
      <ellipse cx="114" cy="302" rx="112" ry="12" fill="url(#shadow-front)"/>
      <circle cx="114" cy="190" r="110" fill="var(--white)"/>
      <path d="M108 72 C104 40 130 10 182 2 C182 40 158 70 108 72 Z" fill="var(--green)"/>
    </svg>
    <div class="volume-badge"></div>
    <div class="tree-illustration" role="img" aria-label="Illustration of a slender orange tree with green leaves, oranges and grass at its base"></div>
    <div class="variety-label">
      <span class="line--green">Tropical</span>
      <span class="line--orange">Orange</span>
      <span class="line--orange">Juice</span>
    </div>
  </section>

  <section class="panel panel--side">
    <div class="top-band"></div>
    <div class="brand-name">Orvelo</div>
    <h2 class="product-title">orange<br>juice</h2>
    <p class="product-copy">Donec eu pharetra lacus mollis blandit neque vulputate semper</p>
    <svg class="fruit" viewBox="0 0 230 320" aria-hidden="true">
      <defs>
        <radialGradient id="shadow-side" cx="50%" cy="50%" r="50%">
          <stop offset="0%" stop-color="#bdbdbd"/>
          <stop offset="100%" stop-color="#bdbdbd" stop-opacity="0"/>
        </radialGradient>
      </defs>
      <ellipse cx="114" cy="302" rx="112" ry="12" fill="url(#shadow-side)"/>
      <circle cx="114" cy="190" r="110" fill="var(--white)"/>
      <path d="M108 72 C104 40 130 10 182 2 C182 40 158 70 108 72 Z" fill="var(--green)"/>
    </svg>
    <div class="volume-badge"></div>
    <div class="tree-illustration" role="img" aria-label="Illustration of a slender orange tree with green leaves, oranges and grass at its base"></div>
    <div class="variety-label">
      <span class="line--green">Tropical</span>
      <span class="line--orange">Orange</span>
      <span class="line--orange">Juice</span>
    </div>
  </section>
</main>
</body>
</html>
```